ORVI LTH website - sleek, sophisticated, uplifting

ORVI Institute for Restorative Care is a cutting-edge medical clinic aimed at providing treatment for various chronic conditions and help people stave off the declines usually associated with aging. We utilize the latest technology in regenerative medicine to help people with autoimmune conditions, musculoskeletal problems and chronic pain, neurodegenerative conditions, male enhancement, facial rejuvenation and hair restoration, etc. We provide personalized medicine, through highly compassionate and competent doctors and staff.

please look at my current website which is not focused on regenerative medicine, but some contents can stay, as far as the philosophy of the treatment: www.pbmosaicwellness-example.com. But the reason I am changing the name of the clinic is because the focus of the medical practice is shifted entirely to "regenerative medicine" - using the body's own healing mechanism such as stem cells and growth factors...

Please DO NOT recycle old graphics and pictures. I want this site to be brand new, fresh and original.

Would like the website to be more sophisticated and nicer-looking than this website: www.duskmere-example.com

Target Market(s)

People who care a great deal about their health (above age 35), wants to prevent declines in their looks and health as they are getting older. Generally high income sector of the society that can afford self-pay (no insurance accepted) expensive stem cell treatment ranging from $4000 to $20,000.

Industry/Entity Type

Healthcare

Coding

Coded - Design and coding required

Number of Pages Required

5+ page

Font styles to use
Sans Serif
Other font styles liked:
• Al Bayan, Avenir, Didot, Open Sans or Tsukushi A Round Gothic for central text, but may use Chalkboard for titles, or others as seen fit

Colors

Designer to choose colors to be used in the design.

Requirements
Must have
• Ultra modern look, very clean & sleek images and layout, portraying a sense of sophistication and confidence. Works beautifully well with existing logo. Give a sense that the clinic employs cutting-edge science, and provide highly competent & compassionate services.
• More sophisticated and nicer-looking than this website: www.duskmere-example.com
Nice to have
• many pages and links to science articles
Should not have
• fonts too playful or hard to read.

```html
<!DOCTYPE html>
<html lang="en">
<head>
<meta charset="utf-8">
<title>ORVI Institute for Restorative Care</title>
<link href="https://fonts.googleapis.com/css2?family=Montserrat:wght@400;500;600;700&display=swap" rel="stylesheet">
<style>
:root{
  --gold:#d19f2c;
  --gold-bright:#f6cf0f;
  --ink:#1c1c1c;
  --body:#444;
  --white:#fff;
  --black:#000;
  --muted:#8a8a8a;
  --info:#f3ead2;
}
*{box-sizing:border-box;margin:0;padding:0}
html,body{width:1200px;height:3495px;overflow:hidden}
body{font-family:'Montserrat',sans-serif;color:var(--body);background:var(--white)}
section,header,footer{position:relative;width:1200px}
.btn{display:inline-block;background:var(--gold-bright);color:var(--ink);font-weight:700;font-size:14px;letter-spacing:2px;text-transform:uppercase;width:150px;height:34px;line-height:34px;text-align:center;text-decoration:none}
.section-title{font-size:32px;font-weight:500;letter-spacing:5px;text-align:center;color:var(--ink);line-height:40px}
.divider{display:flex;align-items:center;justify-content:center;gap:12px;margin-top:14px}
.divider span{width:44px;height:1px;background:#c9a24a}
.divider i{width:12px;height:12px;background:var(--gold-bright)}

/* hero */
.hero{height:610px;background:radial-gradient(circle at 50% 40%,#b7c3e8 0%,#8f9fd6 45%,#6f7cc4 75%,#a890c8 100%)}
.hero-art{position:absolute;inset:0}
.menu{position:absolute;top:28px;right:80px;width:26px}
.menu span{display:block;height:4px;background:var(--ink);margin-bottom:4px}
.brand{position:absolute;top:282px;left:0;width:100%;text-align:center;color:var(--ink)}
.brand-name{font-size:64px;font-weight:700;letter-spacing:2px;line-height:1}
.brand-name::before{content:"";display:inline-block;width:20px;height:20px;background:var(--gold-bright);margin-right:14px;vertical-align:middle}
.brand-sub{font-size:13px;font-weight:600;margin-top:6px}
.hero-title{position:absolute;top:396px;width:100%;text-align:center;color:var(--white);font-size:32px;font-weight:700;letter-spacing:2px;line-height:46px;text-transform:uppercase}

/* about */
.about{height:357px;padding-top:56px;text-align:center}
.about p{width:1030px;margin:26px auto 22px;font-size:14px;line-height:23px;letter-spacing:.6px;text-align:justify;text-align-last:center}

/* services */
.services{height:730px;background:var(--gold);padding-top:56px}
.services h2{color:var(--white);font-size:29px;font-weight:600;letter-spacing:1px;text-align:center;line-height:38px}
.service-grid{display:grid;grid-template-columns:repeat(3,324px);gap:28px;width:1028px;margin:30px auto 0}
.service{position:relative;height:217px;background:linear-gradient(135deg,#8a7b70,#3e3a3a)}
.service.blue{background:linear-gradient(135deg,#1c6f9a,#0a2c48)}
.service.xray{background:linear-gradient(135deg,#5a7fa8,#0c1b30)}
.service.dark{background:linear-gradient(135deg,#3a3230,#0b0b0b)}
.service.face{background:linear-gradient(135deg,#e6d8cf,#9c8476)}
.service.hair{background:linear-gradient(135deg,#6a5a50,#2a2320)}
.service span{position:absolute;left:0;bottom:0;width:100%;height:37px;line-height:37px;background:rgba(0,0,0,.7);color:var(--white);text-align:center;font-size:16px;font-weight:500}
.services .btn{display:block;margin:26px auto 0}

/* audience */
.audience{height:470px;background:linear-gradient(100deg,#06121d 0%,#0d2638 55%,#123447 100%);overflow:hidden}
.audience p{position:absolute;left:93px;top:158px;width:580px;color:var(--gold-bright);font-size:28px;line-height:38px;font-weight:500}
.audience-photo{position:absolute;left:760px;top:20px;width:320px;height:450px;background:radial-gradient(ellipse at 50% 35%,#c09a84 0%,#8d8d93 40%,rgba(18,52,71,0) 75%)}

/* articles */
.articles{height:741px;padding-top:56px}
.article-list{display:flex;gap:26px;width:1028px;margin:40px auto 0}
.article{width:501px;height:470px;border:1px solid #ddd}
.article-img{height:282px;background:linear-gradient(180deg,#101010,#2a1d24)}
.article-img.finger{background:linear-gradient(160deg,#f1eeec 0%,#e4d6cf 45%,#d2b3a4 75%,#e9e4e1 100%)}
.article-body{padding:16px 16px 0}
.article h3{font-size:16px;font-weight:700;letter-spacing:1px;line-height:22px;color:var(--ink);text-transform:uppercase}
.meta{font-size:12px;color:var(--gold);margin:8px 0 10px}
.meta b{font-weight:500;margin:0 10px;color:var(--muted)}
.article p{font-size:13px;line-height:22px;letter-spacing:.5px}
.article p a{color:var(--gold);font-weight:600;text-decoration:underline;letter-spacing:1px}
.articles .btn{display:block;margin:28px auto 0}

/* contact */
.contact{height:385px;background:var(--gold)}
.contact h4{color:var(--white);font-size:20px;font-weight:600;letter-spacing:1px;margin-bottom:20px;text-transform:uppercase;line-height:24px}
.contact-form{position:absolute;left:86px;top:58px;width:324px}
.field{height:34px;background:var(--white);margin-bottom:12px;font-size:13px;color:var(--muted);padding:9px 10px}
.field.message{height:66px}
.contact-form .btn{width:150px;margin-top:6px}
.contact-info{position:absolute;left:438px;top:58px;width:324px}
.contact-info dt{color:var(--gold-bright);font-size:13px;font-weight:600}
.contact-info dd{color:var(--info);font-size:14px;line-height:22px;margin-bottom:14px}
.map{position:absolute;left:790px;top:61px;width:324px;height:261px;background:linear-gradient(135deg,#eeeae2,#dcd8d0)}
.map svg{position:absolute;left:150px;top:105px}
.to-top{position:absolute;right:86px;bottom:-17px;width:35px;height:35px;background:var(--gold-bright);z-index:2}

/* footer */
.site-footer{height:202px;background:var(--black);text-align:center;padding-top:52px}
.footer-brand{color:var(--white);font-size:40px;font-weight:700;letter-spacing:2px;line-height:48px}
.footer-brand::before{content:"";display:inline-block;width:14px;height:14px;background:var(--gold-bright);margin-right:10px;vertical-align:middle}
.copyright{color:var(--white);font-size:13px;margin-top:40px;letter-spacing:.5px}
</style>
</head>
<body>

<header class="hero">
  <div class="hero-art" role="img" aria-label="Soft blue microscopic cells floating in light"></div>
  <div class="menu"><span></span><span></span><span></span></div>
  <div class="brand">
    <div class="brand-name">ORVI</div>
    <div class="brand-sub">ORVI Institute for Restorative Care</div>
  </div>
  <h1 class="hero-title">We utilize the latest technology in<br>regenerative medicine</h1>
</header>

<section class="about">
  <h2 class="section-title">ABOUT US</h2>
  <div class="divider"><span></span><i></i><span></span></div>
  <p>ORVI Institute for Restorative Care is a cutting-edge medical clinic aimed at providing treatment for various chronic conditions and help people stave off the declines usually associated with aging. We utilize the latest technology in regenerative medicine to help people with autoimmune conditions, musculoskeletal problems and chronic pain, neurodegenerative conditions, male enhancement, facial rejuvenation and hair restoration, etc. We provide personalized medicine, through highly compassionate and competent doctors and staff.</p>
  <a class="btn" href="#">Read more</a>
</section>

<section class="services">
  <h2>We utilize the latest technology in regenerative medicine to help<br>people followings problems:</h2>
  <div class="service-grid">
    <div class="service" role="img" aria-label="Hands with skin condition"><span>Autoimmune Conditions</span></div>
    <div class="service blue" role="img" aria-label="Illustrated skeleton with highlighted joint pain"><span>Musculoskeletal Problems</span></div>
    <div class="service xray" role="img" aria-label="Skull x-ray scans"><span>Chronic Pain</span></div>
    <div class="service dark" role="img" aria-label="Man in dim light"><span>Male Enhancement</span></div>
    <div class="service face" role="img" aria-label="Facial treatment at a clinic"><span>Facial Rejuvenation</span></div>
    <div class="service hair" role="img" aria-label="Close-up of hair"><span>Hair Restoration</span></div>
  </div>
  <a class="btn" href="#">View all</a>
</section>

<section class="audience">
  <p>People who care a great deal about their health (above age 35), wants to prevent declines in their looks and health as they are getting older.</p>
  <div class="audience-photo" role="img" aria-label="Smiling mature man listening to music with earphones"></div>
</section>

<section class="articles">
  <h2 class="section-title">SCIENCE ARTICLES</h2>
  <div class="divider"><span></span><i></i><span></span></div>
  <div class="article-list">
    <article class="article">
      <div class="article-img" role="img" aria-label="Anatomical diagram of mercury absorption in the body"></div>
      <div class="article-body">
        <h3>Elan Varrow: The Three Pillars of Heavy Metal Detoxification</h3>
        <div class="meta">Dr. Halvers<b>I</b>halvershealth-example.com<b>I</b>Sun, 19 Jun 2016 14:05 UTC</div>
        <p>Mercury is a pernicious neurotoxin. Removing it, however, needs to be done with great care, lest you cause even more problems. Elan Varrow, Ph.D., is probably one of the foremost experts in the world on the subject... <a href="#">READ MORE</a></p>
      </div>
    </article>
    <article class="article">
      <div class="article-img finger" role="img" aria-label="Close-up photo of a drop of blood on a fingertip"></div>
      <div class="article-body">
        <h3>Blood from human teens rejuvenates body and brains of old mice</h3>
        <div class="meta">Dr. Miren Castell<b>I</b>San Diego</div>
        <p>Blood plasma from young people has been found to rejuvenate old mice, improving their memory, cognition, and physical activity. The method has the potential to be developed into a treatment for people... <a href="#">READ MORE</a></p>
      </div>
    </article>
  </div>
  <a class="btn" href="#">View all</a>
</section>

<section class="contact">
  <div class="contact-form">
    <h4>Contact Form</h4>
    <div class="field">Name</div>
    <div class="field">Email</div>
    <div class="field message">Message</div>
    <a class="btn" href="#">Submit</a>
  </div>
  <div class="contact-info">
    <h4>Contact Info</h4>
    <dl>
      <dt>Address</dt><dd>1200 Larkspur Avenue Suite 400 Fenwood Hills CA 90000</dd>
      <dt>Phone</dt><dd>+1 555 010 2770</dd>
      <dt>Email</dt><dd>info@orvicenter-example.com</dd>
    </dl>
  </div>
  <div class="map" role="img" aria-label="Street map showing the clinic location">
    <svg width="24" height="34" viewBox="0 0 24 34"><path d="M12 0C5 0 0 5 0 12c0 9 12 22 12 22s12-13 12-22C24 5 19 0 12 0z" fill="#d93025"/><circle cx="12" cy="12" r="4" fill="#8a1a12"/></svg>
  </div>
  <a class="to-top" href="#" aria-label="Back to top"><svg width="35" height="35" viewBox="0 0 35 35"><path d="M10 21l7.5-8 7.5 8" fill="none" stroke="#1c1c1c" stroke-width="3"/></svg></a>
</section>

<footer class="site-footer">
  <div class="footer-brand">ORVI</div>
  <p class="copyright">Copyright © 2017 &nbsp;I&nbsp; All Rights Reserved.</p>
</footer>

</body>
</html>
```